Business Card Design Project

Small privately owned salon.

Industry/Entity Type

Business

Contact Information for Business Card

Hair salon.i would like my logo to be my name , Rosalind Marie. Address and phone can go on the front or back. The back will be where I write their appt.
address-527 Willowbend lane Ashford, Oh. 44521
Phone- 717-464-3082

```html
<!DOCTYPE html>
<html lang="en">
<head>
<meta charset="utf-8">
<title>Rosalind Marie – Business Card</title>
<link rel="stylesheet" href="https://fonts.googleapis.com/css2?family=Great+Vibes&family=Open+Sans:ital,wght@0,400;0,700;1,400&display=swap">
<style>
  :root {
    --page-bg: #e7e3e1;
    --card-top: #f1ecea;
    --band-dark: #333333;
    --card-white: #ffffff;
    --accent-gold: #e9c31b;
    --text-light: #ffffff;
    --text-dark: #1e1e1e;
    --emblem-tone: #8f8b8a;
  }
  * { margin: 0; padding: 0; box-sizing: border-box; }
  html, body { width: 1200px; height: 900px; overflow: hidden; }
  body {
    position: relative;
    background: var(--page-bg);
    font-family: "Open Sans", Arial, sans-serif;
  }
  .card {
    position: absolute;
    overflow: hidden;
    box-shadow: 0 6px 18px rgba(0,0,0,0.18);
  }
  .card--front { left: 238px; top: 62px; width: 555px; height: 342px; }
  .card--back  { left: 457px; top: 518px; width: 560px; height: 343px; }

  .card__top {
    position: absolute; left: 0; top: 0; width: 100%;
    background: var(--card-top);
  }
  .card--front .card__top { height: 185px; }
  .card--back  .card__top { height: 187px; }

  .emblem {
    position: absolute; top: 16px; left: 50%;
    width: 150px; height: 150px; margin-left: -75px;
    border-radius: 50%;
    background: radial-gradient(circle, var(--emblem-tone) 0%, rgba(143,139,138,0.35) 60%, rgba(143,139,138,0) 72%);
  }

  .card__band {
    position: absolute; left: 0; top: 185px; width: 100%; height: 157px;
    background: var(--band-dark);
  }
  .owner-name {
    position: absolute; left: 38px; top: 54px;
    font-family: "Great Vibes", cursive;
    font-size: 38px; color: var(--accent-gold); white-space: nowrap;
  }
  .contact {
    position: absolute; left: 298px; top: 38px;
    color: var(--text-light); font-size: 17px; line-height: 24px;
  }
  .contact__phone { display: flex; align-items: center; gap: 12px; margin-bottom: 16px; }
  .contact__phone svg { width: 15px; height: 15px; }

  .card__form {
    position: absolute; left: 0; top: 187px; width: 100%; height: 156px;
    background: var(--card-white); color: var(--text-dark);
  }
  .form-line {
    position: absolute; left: 100px; width: 360px;
    display: flex; align-items: baseline;
    font-size: 14px; font-weight: 700;
  }
  .form-line--name { top: 26px; }
  .form-line--date { top: 67px; }
  .form-line__dots {
    flex: 1; border-bottom: 2px dotted var(--text-dark);
    margin: 0 2px 0 6px; transform: translateY(-3px);
  }
  .form-line__dots--short { flex: 0 0 108px; margin-left: 2px; }
  .notice {
    position: absolute; left: 0; top: 111px; width: 100%;
    text-align: center; font-style: italic; font-size: 13px;
  }
</style>
</head>
<body>
  <section class="card card--front">
    <div class="card__top">
      <div class="emblem" role="img" aria-label="Salon emblem: crossed scissors and comb with flourishes"></div>
    </div>
    <div class="card__band">
      <div class="owner-name">Rosalind Marie</div>
      <div class="contact">
        <div class="contact__phone">
          <svg viewBox="0 0 24 24" aria-hidden="true"><path fill="#e9c31b" d="M6.6 10.8a15.1 15.1 0 0 0 6.6 6.6l2.2-2.2c.3-.3.7-.4 1-.2 1.1.4 2.3.6 3.6.6.6 0 1 .4 1 1V20c0 .6-.4 1-1 1C10.6 21 3 13.4 3 4c0-.6.4-1 1-1h3.5c.6 0 1 .4 1 1 0 1.3.2 2.5.6 3.6.1.3 0 .7-.2 1z"/></svg>
          <span>717-464-3082</span>
        </div>
        <div class="contact__address">527 Willowbend lane Ashford, Oh.<br>44521</div>
      </div>
    </div>
  </section>

  <section class="card card--back">
    <div class="card__top">
      <div class="emblem" role="img" aria-label="Salon emblem: crossed scissors and comb with flourishes"></div>
    </div>
    <div class="card__form">
      <div class="form-line form-line--name"><span>Name:</span><span class="form-line__dots"></span></div>
      <div class="form-line form-line--date"><span>Date:</span><span class="form-line__dots"></span><span>Time:</span><span class="form-line__dots form-line__dots--short"></span></div>
      <p class="notice">If unable to keep appointment,&nbsp; kindly give 24hrs notice.</p>
    </div>
  </section>
</body>
</html>
```